Patent Law

Need to develop a home page for a patent lawyer.

Colors should go with logo, blues...

Company Name- Corvel Tindry, PLLC

Company Overview-

I am an Intellectual Property Lawyer and focus on patents, copyrights, trademarks, & trade secrets. I work with small businesses and start ups in the chemical and biotech industries.

Why Us-

I am small firm that can provide large-firm service at a reasonable price. I also can charge flat-fees for entreprenuers in certain practice areas.

Services-
Intellectual Property
Patents
Copyrights
Trademarks
Trade secrets
Healthcare Compliance
Elder law
Wills
Trusts

Website we like-
http://www.quarnlowtide.example/ - within industry!!
http://www.vopperhask.example/
http://dulbrickovan.example/
http://thefernwoldguides.example/

Target Market(s)

My customers will be small business, specifically small start-up companies in the chemical and biotech arena.

Industry/Entity Type

Trade

Requirements
Must have
• Colors should go with logo, blues...

```html
<!DOCTYPE html>
<html lang="en">
<head>
<meta charset="utf-8">
<title>Corvel Tindry, PLLC — Intellectual Property Law</title>
<link rel="stylesheet" href="https://fonts.googleapis.com/css2?family=Questrial&display=swap">
<style>
:root{
  --blue-deep:#1d5f8c;
  --blue-mid:#2c79ad;
  --blue-band:#1f6a9b;
  --blue-accent:#2d98d6;
  --blue-light:#5cb6ea;
  --gray-page:#f1f1f1;
  --gray-why:#e2e2e2;
  --gray-text:#7a7a7a;
  --footer-dark:#2b2b2b;
  --footer-black:#0b0b0b;
  --white:#ffffff;
}
*{margin:0;padding:0;box-sizing:border-box}
html,body{width:791px;height:1200px;overflow:hidden;background:var(--gray-page)}
body{font-family:"Questrial",Arial,sans-serif;color:var(--white)}
.page{position:relative;width:800px;height:1213px;transform:scale(0.98875);transform-origin:0 0;background:var(--gray-page)}
.abs{position:absolute}

.top-strip{left:0;top:0;width:800px;height:5px;background:var(--blue-mid)}
.header{left:0;top:5px;width:800px;height:55px;background:linear-gradient(#fafafa,#eeeeee)}
.social{display:flex;gap:4px}
.social span{width:19px;height:19px;border-radius:50%;background:var(--blue-accent);display:block}
.header-social{left:576px;top:29px}
.search{left:652px;top:28px;width:97px;height:22px;border:1px solid #b9b9b9;border-radius:3px;background:var(--white);color:#a7a7a7;font-size:11px;padding:4px 7px}
.search svg{position:absolute;right:6px;top:5px}

.nav-band{left:0;top:60px;width:800px;height:32px;background:linear-gradient(#4e93c2,#1f6a9b 55%,#1a5e8b)}
.nav{right:55px;top:69px;display:flex;font-size:11px;letter-spacing:.8px}
.nav a{color:var(--white);text-decoration:none;margin-left:36px}
.nav a:first-child{margin-left:0}

.logo-box{left:82px;top:35px;width:97px;height:73px;background:linear-gradient(135deg,#ffffff,#d8d8d8);border:1px solid #c9c9c9;box-shadow:0 2px 4px rgba(0,0,0,.35);display:flex;flex-direction:column;align-items:center;justify-content:center;gap:5px}
.logo-box .mark{width:16px;height:16px;background:var(--blue-deep)}
.logo-name{font-size:8.5px;color:#3b3b3b;letter-spacing:.2px;white-space:nowrap}

.services-band{left:0;top:333px;width:800px;height:474px;background:linear-gradient(180deg,#1b5883,#1e6594 50%,#1b5c89)}

.hero{left:60px;top:98px;width:689px;height:311px;background:linear-gradient(120deg,#2a2a2e 0%,#3a3633 35%,#c9c1b3 60%,#e9e6e2 100%)}
.hero-caption{left:60px;top:311px;width:689px;height:98px;background:rgba(25,25,25,.82)}
.hero-caption h2{position:absolute;left:119px;top:11px;font-size:12px;font-weight:normal;color:var(--blue-light);letter-spacing:.8px}
.hero-caption p{position:absolute;left:121px;top:31px;width:475px;font-size:10.5px;line-height:13.5px;letter-spacing:.6px;color:#f0f0f0}
.dots{left:696px;top:388px;display:flex;gap:5px}
.dots span{width:8px;height:8px;border-radius:50%;background:var(--white)}
.dots span.active{background:var(--blue-accent)}
.arrow{font-size:30px;line-height:1}

.section-title{left:0;width:800px;text-align:center;font-size:17px;font-weight:normal;letter-spacing:1.6px}
.rule{height:1px}
.services-intro{left:165px;top:469px;width:470px;text-align:center;font-size:11px;line-height:14px;letter-spacing:.5px}

.service{width:150px}
.service .photo{width:128px;height:128px;border-radius:50%;border:4px solid var(--blue-accent);margin-left:-6px}
.service h3{margin-top:14px;font-size:11px;font-weight:normal;letter-spacing:.8px}
.service p{margin-top:6px;width:132px;font-size:9.3px;line-height:13.5px;letter-spacing:.4px}
.service a{display:block;margin-top:6px;font-size:10px;letter-spacing:.6px;color:var(--blue-light);text-decoration:none}

.why{left:0;top:807px;width:800px;height:190px;background:linear-gradient(#f2f2f2,#dcdcdc)}
.why-text{left:150px;top:889px;width:512px;font-size:13px;line-height:15px;letter-spacing:.8px;color:var(--gray-text)}

.footer{left:0;top:997px;width:800px;height:194px;background:linear-gradient(#444,#262626 60%,#1c1c1c)}
.footer-heading{font-size:12px;font-weight:normal;letter-spacing:1px}
.field{background:var(--white);border:1px solid #bbb;border-radius:2px}
.submit{left:124px;top:1142px;width:112px;height:20px;background:linear-gradient(#3b8bc3,#1d6597);font-size:10px;letter-spacing:1px;text-align:center;line-height:20px}
.footer-logo{left:300px;top:1025px;width:200px;height:130px;background:radial-gradient(ellipse at center,rgba(120,120,120,.75) 0%,rgba(60,60,60,.3) 50%,rgba(0,0,0,0) 72%);display:flex;flex-direction:column;align-items:center;justify-content:center;gap:6px}
.footer-logo .mark{width:18px;height:18px;background:var(--blue-deep)}
.footer-logo .logo-name{color:#1e1e1e;font-size:9.5px}
.location{left:557px;top:1041px;font-size:9.5px;line-height:12px;letter-spacing:.5px}
.location .label{color:var(--blue-light)}
.footer-social{left:557px;top:1147px}
.footer-social span{width:17px;height:17px}
.copyright-bar{left:0;top:1191px;width:800px;height:22px;background:var(--footer-black);text-align:center;font-size:9.5px;line-height:22px;letter-spacing:.6px}
</style>
</head>
<body>
<div class="page">
  <div class="abs top-strip"></div>
  <header class="abs header"></header>
  <div class="abs social header-social"><span></span><span></span><span></span></div>
  <div class="abs search">Search
    <svg width="12" height="12" viewBox="0 0 12 12"><circle cx="5" cy="5" r="3.5" fill="none" stroke="#aaa" stroke-width="1.4"/><line x1="7.5" y1="7.5" x2="11" y2="11" stroke="#aaa" stroke-width="1.6"/></svg>
  </div>
  <div class="abs nav-band"></div>
  <nav class="abs nav"><a href="#">HOME</a><a href="#">ABOUT &nbsp;US</a><a href="#">OUR SERVICES</a><a href="#">CONTACT US</a></nav>
  <div class="abs logo-box"><span class="mark"></span><span class="logo-name">Corvel Tindry, PLLC</span></div>

  <div class="abs services-band"></div>

  <div class="abs hero" role="img" aria-label="Lawyer in a dark suit and red tie leafing through a book at a desk"></div>
  <div class="abs hero-caption">
    <h2>WELCOME TO CORVEL TINDRY PLLC</h2>
    <p>I am an Intellectual Property Lawyer and focus on patents, copyrights, trademarks, &amp; trade secrets. I work with small businesses and start ups in the chemical and biotech industries.</p>
  </div>
  <div class="abs arrow" style="left:72px;top:237px;color:var(--blue-mid)">&#10094;</div>
  <div class="abs arrow" style="left:722px;top:237px;color:var(--blue-mid)">&#10095;</div>
  <div class="abs dots"><span></span><span></span><span class="active"></span></div>

  <h2 class="abs section-title" style="top:421px">OUR SERVICES</h2>
  <div class="abs rule" style="left:235px;top:451px;width:330px;background:linear-gradient(90deg,transparent,#5d9ac4,transparent)"></div>
  <p class="abs services-intro">Lorem ipsum dolor sit amet, consectetur adipiscing elit. Duis ut risus quis felis vestibulum accumsan. Nam sem lorem, dapibus a cursus vel, bibendum ut orci. Maecenas lectus lectus, lacinia in fringilla laoreet.</p>

  <div class="abs arrow" style="left:70px;top:602px;color:#8aa3b6">&#10094;</div>
  <div class="abs arrow" style="left:727px;top:602px;color:var(--blue-accent)">&#10095;</div>

  <div class="abs service" style="left:167px;top:553px">
    <div class="photo" role="img" aria-label="Wooden judge's gavel resting on printed papers" style="background:radial-gradient(circle at 45% 45%,#7a4a2c,#c9b9a6 60%,#efe9e2)"></div>
    <h3>PATENTS SERVICE</h3>
    <p>Lorem ipsum dolor sit amet, consectetur adipiscing elit. Duis ut risus oquis afelis</p>
    <a href="#">Read more &#10095;</a>
  </div>
  <div class="abs service" style="left:351px;top:553px">
    <div class="photo" role="img" aria-label="Copyright symbol on a blue grid" style="background:radial-gradient(circle at 50% 50%,#5b86b8,#a9c6e6 60%,#dbe8f5)"></div>
    <h3>COPYRIGHT SERVICE</h3>
    <p>Lorem ipsum dolor sit amet, consectetur adipiscing elit. Duis ut risus oquis afelis</p>
    <a href="#">Read more &#10095;</a>
  </div>
  <div class="abs service" style="left:532px;top:553px">
    <div class="photo" role="img" aria-label="Gold padlock beside large silver trademark letters" style="background:radial-gradient(circle at 50% 40%,#c9a54a,#b8b8b8 55%,#f4f4f4)"></div>
    <h3>TRADEMARKS SERVICE</h3>
    <p>Lorem ipsum dolor sit amet, consectetur adipiscing elit. Duis ut risus oquis afelis</p>
    <a href="#">Read more &#10095;</a>
  </div>

  <section class="abs why"></section>
  <h2 class="abs section-title" style="top:839px;color:var(--blue-accent)">WHY US</h2>
  <div class="abs rule" style="left:270px;top:868px;width:260px;background:linear-gradient(90deg,transparent,#c4c4c4,transparent)"></div>
  <p class="abs why-text">I am small firm that can provide large-firm service at a reasonable price. I also can charge flat-fees for entreprenuers in certain practice areas.</p>

  <footer class="abs footer"></footer>
  <h4 class="abs footer-heading" style="left:123px;top:1018px">QUICK CONTACT</h4>
  <div class="abs field" style="left:124px;top:1041px;width:113px;height:18px"></div>
  <div class="abs field" style="left:124px;top:1065px;width:113px;height:18px"></div>
  <div class="abs field" style="left:124px;top:1089px;width:113px;height:48px"></div>
  <div class="abs submit">SUBMIT</div>

  <div class="abs footer-logo"><span class="mark"></span><span class="logo-name">Corvel Tindry, PLLC</span></div>

  <h4 class="abs footer-heading" style="left:555px;top:1019px">LOCATION</h4>
  <div class="abs location">
    <div><span class="label">Address:</span> 123 Lorem Ipsum</div>
    <div>Address, Street, City</div>
    <div>Code Country</div>
    <div style="margin-top:11px"><span class="label">Tel:</span> (02)-1234-5678</div>
    <div><span class="label">Mobile:</span> (02)-1234-5679</div>
    <div style="margin-top:11px"><span class="label">Email:</span> your@email.com</div>
  </div>
  <div class="abs social footer-social"><span></span><span></span><span></span><span></span></div>

  <div class="abs copyright-bar">Copyright © 2014 CORVEL TINDRY. PLLC</div>
</div>
</body>
</html>
```